Postcard Design Spring Trails D to D

Residential Real Estate, we want to implement a mail campaign in an specific geographic area.We want to include Market information on the area and statistics of the real estate market.This piece is going to be deliver via mail service door to door.

Target Market(s)

Home owners that might be interested in selling their houses

Industry/Entity Type

Real Estate

Font styles to use
Sans Serif

Colors
ec1f27
f78f20

Requirements
Must have
• Attractive look
• Include the information that we just sent to you
• Clear graphics and tables
• Must include clear information about our group

```html
<!DOCTYPE html>
<html lang="en">
<head>
<meta charset="utf-8">
<title>Spring Trails Market Report – October 2015</title>
<link rel="stylesheet" href="https://fonts.googleapis.com/css2?family=Source+Sans+3:ital,wght@0,400;0,600;0,700;1,400;1,600&display=swap">
<style>
  :root {
    --red: #ec1f27;
    --red-dark: #c8141b;
    --orange: #f78f20;
    --blue: #1f6fb5;
    --ink: #3a3a3a;
    --soft: #f4f4f4;
    --white: #ffffff;
  }
  * { margin: 0; padding: 0; box-sizing: border-box; }
  html, body { width: 1200px; height: 929px; overflow: hidden; background: var(--white); }
  body { font-family: "Source Sans 3", Arial, sans-serif; color: var(--ink); }

  .postcard { position: relative; width: 1200px; height: 929px; overflow: hidden; background: var(--white); }

  .header-band { position: absolute; left: 0; top: 0; width: 1200px; height: 150px; }
  .brand-title {
    position: absolute; left: 48px; top: 8px;
    font-size: 66px; font-weight: 400; color: var(--white); letter-spacing: 0.5px;
  }
  .issue-date {
    position: absolute; right: 48px; top: 26px;
    font-size: 34px; font-weight: 400; color: var(--white);
  }
  .trend-icon { position: absolute; left: 520px; top: 10px; }

  .report-title {
    position: absolute; left: 0; width: 1200px; top: 104px;
    text-align: center; font-size: 33px; font-weight: 600; color: var(--blue);
  }

  .letter {
    position: absolute; left: 48px; top: 178px; width: 620px;
    font-size: 21px; line-height: 1.3;
  }
  .letter p { margin-bottom: 24px; }
  .letter .indent { padding-left: 26px; }

  .facts-box {
    position: absolute; left: 740px; top: 190px; width: 360px; height: 150px;
    border: 2px solid var(--red); padding: 26px 14px 0 14px;
  }
  .facts-heading {
    position: absolute; left: 50%; top: -18px; transform: translateX(-50%);
    background: var(--white); padding: 0 8px;
    font-size: 26px; font-weight: 600; color: var(--red); white-space: nowrap;
  }
  .facts-table { width: 100%; border-collapse: collapse; font-size: 20px; color: var(--blue); }
  .facts-table td { padding: 2px 0; line-height: 1.15; }
  .facts-table td.value { text-align: right; color: var(--ink); }

  .quote-bubble { position: absolute; left: 728px; top: 378px; }
  .quote-text {
    position: absolute; left: 778px; top: 400px; width: 370px;
    text-align: center; color: var(--white);
    font-size: 25px; font-weight: 600; font-style: italic; line-height: 1.25;
  }

  .partners { position: absolute; left: 0; top: 810px; width: 1200px; height: 80px; }
  .partner-group {
    position: absolute; left: 388px; top: 18px;
    font-size: 28px; font-weight: 600; color: var(--ink);
  }
  .partner-divider { position: absolute; left: 593px; top: 10px; width: 2px; height: 60px; background: #9a9a9a; }
  .partner-agency { position: absolute; left: 612px; top: 6px; display: flex; align-items: center; gap: 10px; }
  .agency-mark { width: 58px; height: 58px; background: var(--red); }
  .agency-name { font-size: 22px; font-weight: 600; color: var(--ink); line-height: 1.05; }

  .footer-band { position: absolute; left: 0; bottom: 0; width: 1200px; height: 50px; }
</style>
</head>
<body>
<main class="postcard">

  <svg class="header-band" viewBox="0 0 1200 150" aria-hidden="true">
    <defs>
      <linearGradient id="headerRed" x1="0" y1="0" x2="0" y2="1">
        <stop offset="0" stop-color="#f0353b"/>
        <stop offset="1" stop-color="#c8141b"/>
      </linearGradient>
    </defs>
    <path d="M0 0 H1200 V64 C900 108 420 74 0 92 Z" fill="url(#headerRed)"/>
    <path d="M0 92 C420 74 900 108 1200 64 V72 C900 116 420 84 0 100 Z" fill="#f78f20" opacity="0.55"/>
  </svg>

  <h1 class="brand-title">Spring Trails</h1>
  <svg class="trend-icon" width="170" height="60" viewBox="0 0 170 60" aria-hidden="true">
    <polyline points="10,46 62,34 112,44 160,14" fill="none" stroke="#ffffff" stroke-width="4"/>
    <circle cx="10" cy="46" r="7" fill="#ffffff"/>
    <circle cx="62" cy="34" r="7" fill="#ffffff"/>
    <circle cx="112" cy="44" r="7" fill="#ffffff"/>
    <circle cx="160" cy="14" r="7" fill="#ffffff"/>
  </svg>
  <div class="issue-date">October 2015</div>

  <h2 class="report-title">Market Report of single family sold and active homes</h2>

  <section class="letter">
    <p>Dear Spring Trails Neighbor:</p>
    <p>We expect that this information will be useful for you to learn about the Real estate market in your neighbor-hood.</p>
    <p>There are 28 properties “Active for Sale” on the market, with an average price of $303,589 USD and $101.06 USD per sf.</p>
    <p class="indent">Average time on market for sale 63 days.</p>
    <p>In process, “Pending to Close” are 9&nbsp; houses at average price of $252,808 USD with a sale price of $103.11 per sf. with 34 Days on market.</p>
    <p>The past 6 Months&nbsp; market behavior was as follows: 97 Houses sold at average price of $263,545 with a sale price / sqf. of $100.50</p>
  </section>

  <section class="facts-box">
    <h3 class="facts-heading">2014 Facts</h3>
    <table class="facts-table">
      <tr><td>Single Family Properties</td><td class="value">1,677</td></tr>
      <tr><td>Median Square Feet</td><td class="value">2,568</td></tr>
      <tr><td>Median Lot Square Feet</td><td class="value">7,689</td></tr>
      <tr><td>Meian Year Built</td><td class="value">2007</td></tr>
    </table>
  </section>

  <svg class="quote-bubble" width="450" height="175" viewBox="0 0 450 175" aria-hidden="true">
    <path d="M40 0 H430 Q450 0 450 20 V140 Q450 160 430 160 H60 L0 172 L28 140 V20 Q28 0 40 0 Z" fill="#f78f20"/>
  </svg>
  <p class="quote-text">“We will be glad to meet with you and have the opportunity to help you with your Real Estate requirements”</p>

  <footer class="partners">
    <div class="partner-group">The Marlow Group</div>
    <div class="partner-divider"></div>
    <div class="partner-agency">
      <div class="agency-mark"></div>
      <div class="agency-name">Brightfield Realty<br>Pine Hollow</div>
    </div>
  </footer>

  <svg class="footer-band" viewBox="0 0 1200 50" aria-hidden="true">
    <path d="M0 22 C400 6 820 36 1200 10 V50 H0 Z" fill="#ec1f27"/>
  </svg>

</main>
</body>
</html>
```